Design ebook cover for my ebook and website logo. Thought Beyond Sores

This is my ebook, website, blog, and vision I have had for 24 years! Its about something that is a mystery to most of us,that is the healing power of your mind. This is both a personal account and true story. It is also a "how to" for the reader and website, blog followers. I envision words like organic, and infinite when describing this power. A theme in my book is visualzation and thoughts being pure potential energy. The book is really about consciously guiding healing throughout one's own body. A huge part of this is somethong called guided imagery. When I guided my healing, i visualized white blood cells and white light engulfing my entire body. Perhaps this can be used in the design. I also envisioned the Herpes Simplex virus as being completley destroyed by my immune system. I describe it as my mind was the commander in chief, my immune system was my battlefield general, my white blood cells were the soildiers, and the herpes simplex virus was the enemy. In my visualization, my white blood cells numbered in the trillions and the Herpes Simplex virus was very low in numbers. Our healing minds are infinitely strong. Herpes is weak by compariosn.
Good luck!

Title
Thought Beyond Sores
Sub Title
"Mending Sores Through The Strength Of Your Thought"
Author's name Dorian K Vellam III

Target Market(s)

18 -26 year old, slightly more female to male ratio. Largest increasing population is white teenagers. New comers are in shock and looking for answers.

Font styles to use
Sans Serif

Colors
0592ce
6c459b
0455a3

Requirements
Must have
• Think organic, of nature and availbale to everyone. the power of our minds is our birthright! Its about harnessing enegy. This book at it's very core is about the power of the imagination.
Nice to have
• Please think "infinite" and "limitless." Something that immediately opens the mind of the reader at first sight. One of the themes in my book is the emotional connection with the virus
Should not have
• I dont want anything generic. Nothing man made such as machinery, plastic, exc....

```html
<!DOCTYPE html>
<html lang="en">
<head>
<meta charset="utf-8">
<title>Thought Beyond Sores – Book Cover</title>
<link href="https://fonts.googleapis.com/css2?family=Oswald:wght@500;600&family=Montserrat:wght@600;700;800&display=swap" rel="stylesheet">
<style>
  :root {
    --stage: #e9e9ea;
    --paper: #f7f7f8;
    --ink-blue: #1c56b4;
    --band-blue: #0f4fa8;
    --box-blue: #0a3f8f;
    --text-dark: #2a2a2e;
    --white: #ffffff;
    --skin-light: #f1d6c6;
    --skin-mid: #d9a88e;
  }
  * { margin: 0; padding: 0; box-sizing: border-box; }
  html, body {
    width: 1200px; height: 800px; overflow: hidden;
    background: var(--stage);
  }
  .stage {
    position: relative; width: 1200px; height: 800px;
    display: flex; justify-content: center; align-items: center; gap: 70px;
  }
  .cover {
    position: relative; width: 400px; height: 600px;
    background: var(--paper);
    box-shadow: 0 10px 30px rgba(0,0,0,0.12);
    overflow: hidden;
  }

  /* Back cover */
  .back-cover { padding: 22px 24px 0; }
  .back-author {
    font-family: "Montserrat", sans-serif; font-weight: 700;
    font-size: 11px; letter-spacing: 2px; color: var(--ink-blue);
    text-align: right;
  }
  .back-title {
    font-family: "Oswald", sans-serif; font-weight: 600;
    font-size: 40px; line-height: 1.05; color: var(--ink-blue);
    text-transform: uppercase; text-align: center; letter-spacing: 0.5px;
    margin-top: 2px;
  }
  .back-subtitle {
    font-family: "Montserrat", sans-serif; font-weight: 800;
    font-size: 11.5px; color: var(--ink-blue); text-align: center;
    margin-top: 4px;
  }
  .back-blurb {
    font-family: "Montserrat", sans-serif; font-weight: 700;
    font-size: 9.4px; line-height: 1.42; color: var(--text-dark);
    text-align: justify; text-align-last: center; margin-top: 12px;
  }
  .back-footer {
    position: absolute; left: 24px; right: 24px; bottom: 22px;
    display: flex; justify-content: space-between;
  }
  .back-slot {
    width: 96px; height: 58px; background: var(--box-blue);
    color: var(--white); font-family: "Montserrat", sans-serif;
    font-weight: 600; font-size: 9px;
    display: flex; align-items: center; justify-content: center;
  }

  /* Front cover */
  .front-cover { background: var(--paper); }
  .front-title {
    position: absolute; top: 14px; left: 0; right: 0;
    font-family: "Oswald", sans-serif; font-weight: 600;
    font-size: 74px; line-height: 0.98; color: var(--ink-blue);
    text-transform: uppercase; text-align: center;
  }
  .front-art {
    position: absolute; left: 30px; right: 30px; top: 262px; bottom: 62px;
    background:
      radial-gradient(ellipse 30% 42% at 50% 40%, var(--skin-light) 0%, rgba(241,214,198,0) 100%),
      linear-gradient(180deg, #6b625e 0%, #c9a896 18%, var(--skin-light) 55%, var(--skin-mid) 100%);
    border-radius: 120px 120px 0 0;
  }
  .front-band {
    position: absolute; left: 0; right: 0; bottom: 0; height: 62px;
    background: var(--band-blue); color: var(--white);
    display: flex; flex-direction: column; align-items: center; justify-content: center;
    text-align: center; padding: 0 10px;
  }
  .front-subtitle {
    font-family: "Montserrat", sans-serif; font-weight: 800; font-size: 12.5px;
  }
  .front-author {
    font-family: "Montserrat", sans-serif; font-weight: 700; font-size: 10.5px;
    letter-spacing: 2.5px; margin-top: 5px;
  }
</style>
</head>
<body>
<main class="stage">
  <section class="cover back-cover" aria-label="Back cover">
    <p class="back-author">Dorian K Vellam III</p>
    <h2 class="back-title">Thought Beyond Sores</h2>
    <p class="back-subtitle">Mending Sores Through The Strength Of Your Thought</p>
    <p class="back-blurb">Lorem ipsum dolor sit amet, consectetur adipisicing elit, sed do eiusmod tempor incididunt ut labore et dolore magna aliqua. Ut enim ad minim veniam, quis nostrud exercitation. Lorem ipsum dolor sit amet, consectetur adipisicing elit, sed do eiusmod tempor incididunt ut labore et dolore magna aliqua. Ut enim ad minim veniam, quis nostrud exercitation. Lorem ipsum dolor sit amet, consectetur adipisicing elit, sed do eiusmod tempor incididunt ut labore et dolore magna aliqua. Ut enim ad minim veniam, quis nostrud exercitation. Lorem ipsum dolor sit amet, consectetur adipisicing elit, sed do eiusmod tempor incididunt ut labore et dolore magna aliqua. Ut enim ad minim veniam, quis nostrud exercitation. Lorem ipsum dolor sit amet, consectetur adipisicing elit, sed do eiusmod tempor incididunt ut labore et dolore magna aliqua. Ut enim ad minim veniam, quis nostrud exercitation. Lorem ipsum dolor sit amet, consectetur adipisicing elit, sed do eiusmod tempor incididunt ut labore et dolore magna aliqua. Ut enim ad minim veniam, quis nostrud exercitation. Lorem ipsum dolor sit amet, consectetur adipisicing elit, sed do eiusmod tempor incididunt ut labore et dolore magna aliqua. Ut enim ad minim veniam, quis nostrud exercitation. Lorem ipsum dolor sit amet, consectetur adipisicing elit, sed do eiusmod tempor incididunt ut labore et dolore magna aliqua.</p>
    <div class="back-footer">
      <div class="back-slot">LOGO</div>
      <div class="back-slot">ISBN</div>
    </div>
  </section>

  <section class="cover front-cover" aria-label="Front cover">
    <h1 class="front-title">Thought<br>Beyond<br>Sores</h1>
    <div class="front-art" role="img" aria-label="Photograph of a calm young woman with closed eyes, fingertips at her temples, the top of her head opened like a bowl beneath the title"></div>
    <div class="front-band">
      <p class="front-subtitle">Mending Sores Through The Strength Of Your Thought</p>
      <p class="front-author">Dorian K Vellam III</p>
    </div>
  </section>
</main>
</body>
</html>
```